PEACFUL ACUPUNCTURE PRACTITIONER NEEDS A NEW COAT

I need a new design for an exiting website http://willowgateneedlework.com/ for a acupuncturist. This will be a minimalism design with lots and lots of white space. Home page and one interior page. Please keep the feeling of calm and peaceful serenity. For Color scheme: https://www.morningfernclinic.com/fertility. The bottom part of the home page with sections and links to the service pages: https://harborlotuswellness.com/. The client likes this the best: http://mfclinic.com/. I'm attaching the logo and content pages.

Target Market(s)

Women

Industry/Entity Type

Wellness, health, wellbeing, meditation

Number of Pages Required

2 page

Font styles to use
Sans Serif
Decorative

Colors

Designer to choose colors to be used in the design.

Requirements
Must have
Nice to have
• Follow new website drafts and links
Should not have
• Busy with bright colors. No poping

```html
<!DOCTYPE html>
<html lang="en">
<head>
<meta charset="utf-8">
<title>Willowgate Needlework</title>
<link rel="stylesheet" href="https://fonts.googleapis.com/css2?family=Raleway:wght@400;600;700&display=swap">
<style>
  :root {
    --ink: #000000;
    --text-grey: #555555;
    --logo-grey: #5a5a5a;
    --icon-grey: #d4d4d4;
    --dot: #444444;
    --petal-pale: #f1e6e8;
    --petal-mid: #e2cdd1;
    --petal-deep: #d6bcc1;
    --bg: #ffffff;
  }
  html, body {
    margin: 0;
    padding: 0;
    overflow: hidden;
    background: var(--bg);
  }
  .page {
    position: relative;
    width: 1200px;
    height: 842px;
    overflow: hidden;
    background: var(--bg);
    font-family: "Raleway", sans-serif;
  }
  .contact {
    position: absolute;
    left: 79px;
    top: 37px;
    font-size: 14px;
    font-weight: 700;
    line-height: 18px;
    color: var(--text-grey);
  }
  .brand {
    position: absolute;
    left: 0;
    width: 1200px;
    top: 50px;
    text-align: center;
    font-size: 34px;
    font-weight: 400;
    letter-spacing: 1px;
    color: var(--logo-grey);
  }
  .top-links {
    position: absolute;
    right: 52px;
    top: 36px;
    display: flex;
    align-items: center;
    gap: 9px;
  }
  .shop-link {
    font-size: 18px;
    font-weight: 700;
    color: var(--text-grey);
    margin-right: 8px;
  }
  .social-dot {
    width: 21px;
    height: 21px;
    border-radius: 50%;
    background: var(--icon-grey);
  }
  .intro {
    position: absolute;
    left: 0;
    width: 1242px;
    top: 139px;
    text-align: center;
    font-size: 15.6px;
    line-height: 21px;
    color: var(--text-grey);
    margin: 0;
  }
  .focus-map {
    position: absolute;
    left: 0;
    top: 0;
  }
  .focus-label {
    position: absolute;
    font-size: 17px;
    line-height: 22px;
    color: var(--ink);
    letter-spacing: 0.3px;
  }
  .main-nav {
    position: absolute;
    top: 724px;
    left: 0;
    width: 1200px;
    height: 60px;
  }
  .nav-item {
    position: absolute;
    transform: translateX(-50%);
    display: flex;
    flex-direction: column;
    align-items: center;
    gap: 8px;
    font-size: 17px;
    font-weight: 700;
    color: var(--ink);
    white-space: nowrap;
  }
  .nav-item::before {
    content: "";
    width: 12px;
    height: 12px;
    border-radius: 50%;
    background: var(--dot);
  }
</style>
</head>
<body>
<div class="page">
  <div class="contact">
    <div>hello@willowgateneedlework.com</div>
    <div>+1 800 555 0142</div>
  </div>

  <div class="brand">Willowgate Needlework</div>

  <div class="top-links">
    <span class="shop-link">Shop</span>
    <span class="social-dot"></span>
    <span class="social-dot"></span>
    <span class="social-dot"></span>
  </div>

  <p class="intro">Acupuncture &amp; Chinese Herbal Medicine are rooted in over 3000 years of history and tradition.<br>As a complete medical system that has remained flexible and relevant we honor what has worked<br>from the past while embracing the medicine of tomorrow.</p>

  <svg class="focus-map" width="1200" height="842" viewBox="0 0 1200 842">
    <defs>
      <radialGradient id="lotus-tone" cx="50%" cy="50%" r="50%">
        <stop offset="0%" stop-color="var(--petal-deep)"/>
        <stop offset="60%" stop-color="var(--petal-mid)"/>
        <stop offset="100%" stop-color="var(--petal-pale)"/>
      </radialGradient>
    </defs>
    <circle cx="600" cy="477" r="193" fill="url(#lotus-tone)" role="img" aria-label="Lotus mandala illustration with four dark petals marking the focus areas"/>
    <g stroke="var(--ink)" stroke-width="1">
      <line x1="381" y1="347" x2="600" y2="347"/>
      <line x1="732" y1="477" x2="943" y2="477"/>
      <line x1="290" y1="477" x2="469" y2="477"/>
      <line x1="600" y1="607" x2="838" y2="607"/>
    </g>
  </svg>

  <div class="focus-label" style="left:381px; top:303px;">HORMONE<br>BALANCE</div>
  <div class="focus-label" style="left:833px; top:432px;">EMONTIONAL<br>WELL&nbsp; BEING</div>
  <div class="focus-label" style="left:290px; top:478px;">FERTILITY &amp;<br>PREGNANCY</div>
  <div class="focus-label" style="left:733px; top:608px;">STRENGHT &amp;<br>STRUCTURE</div>

  <nav class="main-nav">
    <span class="nav-item" style="left:241px;">HOME</span>
    <span class="nav-item" style="left:418px;">ABOUT US</span>
    <span class="nav-item" style="left:609px;">FOCUS AREAS</span>
    <span class="nav-item" style="left:787px; top:-2px;">TESTIMONIALS</span>
    <span class="nav-item" style="left:939px; top:-2px;">CONTACT</span>
  </nav>
</div>
</body>
</html>
```